Wordpress template re-design of current website

We need a WordPress template design and new look for our existing website. Our existing site it located at www.velmoro.com.au We are a tech company and want a fresh, clean modern website that matches our brand, services and logo colors. Our main Services are hospitality solutions, Velmoro TV solution and managed networks, more information on these can come from our existing website.

Target Market(s)

We are a tech company so must have a modern feel for new technology

Industry/Entity Type

It Company

Number of Pages Required

5+ page

Font styles to use
Sans Serif

Requirements
Must have
• Be based on a wordpress templete design and match the services that we have in our existing website, in the testimonials want a place for video testimonials as well as text. Nice clean icons used for graphics to represent services.
Nice to have
• nice visual representation of our services in the way of clean icons etc
Should not have
• Clutter

```html
<!DOCTYPE html>
<html lang="en">
<head>
<meta charset="utf-8">
<title>Velmoro Wireless</title>
<link rel="stylesheet" href="https://fonts.googleapis.com/css2?family=Open+Sans:wght@400;600;700&family=Oswald:wght@400;500&family=Raleway:wght@300&display=swap">
<style>
:root{
  --brand:#1f4f8f;
  --navy:#2b4a74;
  --ink:#333;
  --muted:#666;
  --slate:#3a4a5b;
  --bar:#1c1c1c;
  --footer:#111;
  --light:#f3f3f3;
  --accent:#8fe36a;
  --white:#fff;
  --hero-top:#a7cbe4;
  --hero-bottom:#b27d55;
}
*{margin:0;padding:0;box-sizing:border-box}
html,body{width:1200px;height:2248px;overflow:hidden}
body{font-family:"Open Sans",Arial,sans-serif;color:var(--ink);background:var(--white);position:relative}

/* hero */
.hero{position:absolute;left:0;top:0;width:1200px;height:565px;overflow:hidden}
.hero-scene{position:absolute;inset:0;background:linear-gradient(180deg,var(--hero-top) 0%,var(--hero-bottom) 100%)}
.brand{position:absolute;left:180px;top:22px;display:flex;align-items:center;gap:10px}
.brand-mark{width:34px;height:34px;border-radius:50%;background:var(--brand)}
.brand-name{font-weight:700;font-size:32px;color:var(--brand)}
.nav{position:absolute;left:390px;top:27px;display:flex;gap:24px;font-size:14.5px;color:#1d2d44}
.contact-strip{position:absolute;left:792px;top:22px;display:flex;align-items:center;gap:8px;font-size:14.5px;color:#1d2d44}
.round{width:24px;height:24px;border-radius:50%;background:var(--brand);display:inline-flex;align-items:center;justify-content:center}
.divider{width:1px;height:30px;background:#1d2d44;margin:0 6px}
.slide-title{position:absolute;left:230px;top:233px;width:263px;height:68px;background:var(--white);border-radius:10px 10px 0 0;text-align:center;color:var(--brand);font-size:24px;line-height:28px;padding-top:6px}
.slide-sub{position:absolute;left:230px;top:302px;width:357px;height:55px;background:#1f4a86;color:var(--white);font-size:24px;text-align:center;line-height:55px}
.slide-tag{position:absolute;left:292px;top:355px;width:295px;height:37px;background:#5b6670;color:var(--white);font-size:17px;text-align:center;line-height:37px}
.slide-arrow{position:absolute;top:285px;width:40px;height:40px;background:#222;display:flex;align-items:center;justify-content:center}

/* intro & services */
.intro-title{position:absolute;left:0;top:590px;width:1200px;text-align:center;font-family:"Oswald",sans-serif;font-weight:500;font-size:20px;color:var(--brand)}
.intro-sub{position:absolute;left:0;top:621px;width:1200px;text-align:center;font-size:11.5px;color:var(--muted)}
.intro-rule{position:absolute;left:522px;top:643px;width:156px;height:1px;background:#bbb}
.service{position:absolute;width:260px;display:flex;gap:14px}
.service svg{flex:none;margin-top:4px}
.service h3{font-weight:400;font-size:15px;color:var(--brand);margin-bottom:4px}
.service p{font-size:10px;line-height:15px;color:var(--muted)}

/* about */
.about{position:absolute;left:0;top:880px;width:1200px;height:277px;background:var(--navy);color:var(--white)}
.about h2{position:absolute;left:173px;top:42px;font-family:"Oswald",sans-serif;font-weight:400;font-size:21px;border-bottom:2px solid var(--white);padding-bottom:2px}
.about p{position:absolute;left:173px;top:86px;width:560px;font-size:12.5px;line-height:19.6px}
.btn-light{position:absolute;left:173px;top:200px;width:70px;height:28px;background:var(--white);color:#222;font-size:11px;font-weight:700;text-align:center;line-height:28px}
.about-photo{position:absolute;left:758px;top:50px;width:269px;height:178px;background:linear-gradient(135deg,#dfe7ee,#9fb3c6)}

/* testimonials */
.testimonials{position:absolute;left:0;top:1157px;width:1200px;height:401px;background:linear-gradient(90deg,#d4d3d1,#cdbfb2)}
.testimonials h2{position:absolute;left:173px;top:16px;font-weight:400;font-size:20px;color:var(--brand);border-bottom:2px solid var(--brand)}
.video{position:absolute;left:207px;top:98px;width:421px;height:240px;background:linear-gradient(180deg,#5a3a2a,#3b2c24);border-radius:3px;overflow:hidden}
.play{position:absolute;left:182px;top:96px;width:56px;height:38px;background:#e52d27;border-radius:9px}
.play::after{content:"";position:absolute;left:22px;top:11px;border-left:15px solid #fff;border-top:8px solid transparent;border-bottom:8px solid transparent}
.player-bar{position:absolute;left:0;bottom:0;width:100%;height:20px;background:#1a1a1a;font-size:8px;color:#aaa;display:flex;align-items:center;gap:10px;padding:0 8px}
.t-arrow{position:absolute;top:210px;font-size:22px;color:#222}
.quote-card{position:absolute;left:683px;width:344px;height:103px;background:#2d5590;color:var(--white);display:flex;gap:12px;padding:12px}
.avatar{flex:none;width:62px;height:62px;border-radius:50%;background:#b59a82;border:3px solid var(--white);margin-top:8px}
.quote-card p{font-size:10.5px;line-height:15px}
.quote-card .who{color:var(--accent);font-style:italic;font-size:10.5px;line-height:15px;margin-top:6px;font-weight:600}
.mini-nav{position:absolute;top:319px;width:16px;height:16px;background:#111;color:#fff;font-size:10px;text-align:center;line-height:16px}

/* view all & statement */
.view-all{position:absolute;left:0;top:1558px;width:1200px;height:37px;background:var(--bar);color:var(--white);font-size:11px;font-weight:700;text-align:center;line-height:37px;z-index:1}
.view-all::after{content:"";position:absolute;left:592px;top:37px;border-top:9px solid var(--bar);border-left:8px solid transparent;border-right:8px solid transparent}
.statement{position:absolute;left:0;top:1595px;width:1200px;height:197px;background:var(--slate);color:#e6e9ec;font-family:"Raleway",sans-serif;font-weight:300;font-size:27.5px;line-height:34.5px;text-align:center;padding-top:41px}

/* clients */
.clients{position:absolute;left:0;top:1792px;width:1200px;height:145px;background:var(--light)}
.clients h2{position:absolute;left:0;top:14px;width:1200px;text-align:center;font-weight:400;font-size:21px;color:var(--brand)}
.clients h2 span{border-bottom:1px solid var(--brand)}
.client{position:absolute;top:82px;transform:translateX(-50%);display:flex;align-items:center;gap:6px;font-size:15px;font-weight:600;color:#333;white-space:nowrap}
.client i{width:11px;height:11px;background:#333;display:inline-block}

/* footer */
.footer-col{position:absolute;top:1955px}
.footer-col h3{font-weight:400;font-size:19px;color:#333;margin-bottom:14px}
.footer-col p{font-size:10px;line-height:15px;color:#555}
.news-item{display:flex;gap:12px}
.news-thumb{width:58px;height:58px;background:linear-gradient(135deg,#333,#777)}
.news-item h4{font-size:12px;font-weight:600;margin:12px 0 6px}
.meta{font-size:9px;color:#555}
.case-photo{width:193px;height:86px;background:linear-gradient(180deg,#dfe6ec,#9aa9b5)}
.case-title{font-size:12px;font-weight:600;line-height:17px;margin:6px 0 4px;color:#333}
.btn-dark{display:inline-block;margin-top:14px;background:#333;color:#fff;font-size:10px;font-weight:700;padding:4px 9px}
.contact-line{display:flex;gap:12px;font-size:12px;line-height:18px;color:#333;margin-bottom:14px}
.social{display:flex;gap:6px}
.social span{width:20px;height:20px;border:1px solid #9ab;display:inline-block;position:relative}
.social span::after{content:"";position:absolute;left:6px;top:6px;width:6px;height:6px;border-radius:50%;background:var(--brand)}
.social span.alt::after{background:#d9432f}
.bottom-bar{position:absolute;left:0;top:2197px;width:1200px;height:51px;background:var(--footer);color:#aaa;font-size:10.5px;text-align:center;line-height:51px}
.to-top{position:absolute;left:1013px;top:2203px;width:40px;height:40px;background:#3a3a3a;display:flex;align-items:center;justify-content:center}
</style>
</head>
<body>

<header class="hero">
  <div class="hero-scene" role="img" aria-label="Outback landscape photograph with a four-wheel-drive vehicle"></div>
  <div class="brand"><span class="brand-mark"></span><span class="brand-name">Velmoro</span></div>
  <nav class="nav"><span>Home</span><span>About</span><span>Our Services</span><span>Our Work</span><span>Contact</span></nav>
  <div class="contact-strip">
    <span class="round"><svg width="12" height="12" viewBox="0 0 24 24"><path fill="#fff" d="M6.6 10.8c1.4 2.8 3.8 5.1 6.6 6.6l2.2-2.2c.3-.3.7-.4 1-.2 1.1.4 2.3.6 3.6.6.6 0 1 .4 1 1V20c0 .6-.4 1-1 1C10.6 21 3 13.4 3 4c0-.6.4-1 1-1h3.5c.6 0 1 .4 1 1 0 1.3.2 2.5.6 3.6.1.3 0 .7-.2 1z"/></svg></span>
    <span>1300 555 014</span><span class="divider"></span>
    <span class="round"></span><span class="round"></span><span class="round"></span>
  </div>
  <div class="slide-title">Anytime Anywhere<br>Mobile Gateways</div>
  <div class="slide-sub">Full Mobile 3G &amp; 4G Solutions</div>
  <div class="slide-tag">Fast, secure mobile options</div>
  <div class="slide-arrow" style="left:133px"><svg width="12" height="14" viewBox="0 0 12 14"><path d="M10 1 3 7l7 6" fill="none" stroke="#fff" stroke-width="3"/></svg></div>
  <div class="slide-arrow" style="left:1028px"><svg width="12" height="14" viewBox="0 0 12 14"><path d="M2 1l7 6-7 6" fill="none" stroke="#fff" stroke-width="3"/></svg></div>
</header>

<h2 class="intro-title">VELMORO WIRELESS</h2>
<p class="intro-sub">Creating solutions that work</p>
<div class="intro-rule"></div>

<div class="service" style="left:192px;top:694px">
  <svg width="34" height="30" viewBox="0 0 34 30"><circle cx="17" cy="5" r="2.5" fill="#1f3b63"/><path d="M4 22a13 13 0 0 1 26 0z" fill="#1f3b63"/><rect x="1" y="24" width="32" height="3" fill="#1f3b63"/></svg>
  <div><h3>Hospitality Solutions</h3><p>Lorem ipsum dolor sit amet, consectetur adipiscing elit, sed do eiusmod.</p></div>
</div>
<div class="service" style="left:487px;top:694px">
  <svg width="32" height="30" viewBox="0 0 32 30"><path d="M10 2l6 6 6-6" stroke="#1f3b63" stroke-width="2" fill="none"/><rect x="2" y="9" width="28" height="18" rx="2" fill="#1f3b63"/></svg>
  <div><h3>Velmoro TV solution</h3><p>Lorem ipsum dolor sit amet, consectetur adipiscing elit, sed do eiusmod.</p></div>
</div>
<div class="service" style="left:778px;top:694px">
  <svg width="32" height="32" viewBox="0 0 32 32"><path d="M4 8a14 14 0 0 0 20 20z" fill="#1f3b63"/><path d="M14 18l10-10" stroke="#1f3b63" stroke-width="2"/><path d="M20 4a8 8 0 0 1 8 8" stroke="#1f3b63" stroke-width="2" fill="none"/><rect x="10" y="26" width="12" height="4" fill="#1f3b63"/></svg>
  <div><h3>Managed Networks</h3><p>Lorem ipsum dolor sit amet, consectetur adipiscing elit, sed do eiusmod.</p></div>
</div>
<div class="service" style="left:192px;top:780px">
  <svg width="36" height="28" viewBox="0 0 36 28"><path d="M2 10a23 23 0 0 1 32 0" stroke="#1f3b63" stroke-width="4" fill="none"/><path d="M8 16a14 14 0 0 1 20 0" stroke="#1f3b63" stroke-width="4" fill="none"/><circle cx="18" cy="23" r="3.5" fill="#1f3b63"/></svg>
  <div><h3>Social Wi-Fi</h3><p>Lorem ipsum dolor sit amet, consectetur adipiscing elit, sed do eiusmod.</p></div>
</div>
<div class="service" style="left:487px;top:780px">
  <svg width="30" height="34" viewBox="0 0 30 34"><rect x="7" y="1" width="16" height="32" rx="3" fill="#1f3b63"/><rect x="10" y="5" width="10" height="7" fill="#fff"/><g fill="#fff"><rect x="10" y="15" width="3" height="3"/><rect x="14" y="15" width="3" height="3"/><rect x="18" y="15" width="2" height="3"/><rect x="10" y="21" width="3" height="3"/><rect x="14" y="21" width="3" height="3"/><rect x="18" y="21" width="2" height="3"/></g></svg>
  <div><h3>Mining and Remote</h3><p>Lorem ipsum dolor sit amet, consectetur adipiscing elit, sed do eiusmod.</p></div>
</div>
<div class="service" style="left:778px;top:780px">
  <svg width="30" height="34" viewBox="0 0 30 34"><rect x="7" y="1" width="18" height="32" rx="3" fill="none" stroke="#1f3b63" stroke-width="3"/><circle cx="16" cy="28" r="1.8" fill="#1f3b63"/><rect x="2" y="12" width="8" height="8" fill="#1f3b63"/></svg>
  <div><h3>Mobile Solutions</h3><p>Lorem ipsum dolor sit amet, consectetur adipiscing elit, sed do eiusmod.</p></div>
</div>

<section class="about">
  <h2>ABOUT US</h2>
  <p>Velmoro Wireless is at the forefront of revolutionising high-speed internet access (HSIA)<br>services. We offer complete wireless solutions: Right from developing<br>individual components such as hotspots and access controllers, to installation<br>of the internet infrastructure. Once we setup the HSIA for our clients, we back<br>it up with round-the-clock tech support.</p>
  <span class="btn-light">DETAILS</span>
  <div class="about-photo" role="img" aria-label="Office team working with a laptop in a bright workspace"></div>
</section>

<section class="testimonials" aria-label="Testimonials">
  <h2>TESTIMONIAL</h2>
  <span class="t-arrow" style="left:187px">&#8249;</span>
  <div class="video" role="img" aria-label="Video testimonial of a customer seated in a café">
    <span class="play"></span>
    <div class="player-bar"><span>&#10074;&#10074;</span><span>04:24 / 09:35</span><span style="margin-left:auto">360p</span></div>
  </div>
  <span class="t-arrow" style="left:636px">&#8250;</span>
  <div class="quote-card" style="top:98px">
    <span class="avatar" role="img" aria-label="Customer portrait"></span>
    <div><p>The staff at Velmoro have been friendly, helpful and courteous with no problem being too big or small to handle...</p><p class="who">Clara Wynn<br>Strata Manager</p></div>
  </div>
  <div class="quote-card" style="top:210px">
    <span class="avatar" role="img" aria-label="Customer portrait"></span>
    <div><p>Installing Velmoro Internet Solution has been a great investment for this business...</p><p class="who">Tom Reyes<br>Property Manager</p></div>
  </div>
  <span class="mini-nav" style="left:988px">&#8249;</span>
  <span class="mini-nav" style="left:1009px">&#8250;</span>
</section>

<div class="view-all">VIEW ALL</div>
<div class="statement">We strive to out work our competition with an effective<br>approach and a powerful skill set, which is why<br>were industry leading.</div>

<section class="clients">
  <h2><span>OUR CLIENTS</span></h2>
  <span class="client" style="left:233px"><i></i>Harbourline</span>
  <span class="client" style="left:380px">Tandem</span>
  <span class="client" style="left:527px">Norvale</span>
  <span class="client" style="left:674px">Pinehurst</span>
  <span class="client" style="left:820px">Redgum Tours</span>
  <span class="client" style="left:965px">Corvista</span>
</section>

<div class="footer-col" style="left:178px;width:185px">
  <h3>News</h3>
  <div class="news-item"><span class="news-thumb" role="img" aria-label="Hand holding a smartphone"></span><div><h4>New &amp; Improved</h4><span class="meta">Admin &nbsp; 12.11.2015</span></div></div>
  <p style="margin-top:8px">Lorem ipsum dolor sit amet, cituuiscing elit, sed diam nonum oinibh euismdunt ut laoreet [...]</p>
</div>
<div class="footer-col" style="left:390px;width:200px">
  <h3>Case Studies</h3>
  <div class="case-photo" role="img" aria-label="Hospital building exterior"></div>
  <p class="case-title">Kestrel Hospital Patient<br>WI-FI Solution</p>
  <p>Lorem ipsum dolor sit amet, consectetue iscing elit, sed diam nonummy [...]</p>
</div>
<div class="footer-col" style="left:612px;width:200px">
  <h3>Reseller</h3>
  <p>Velmoro is looking for suitably experienced retailers and wholesalers to join our international network of resellers for our internet gateways and wireless [...]</p>
  <span class="btn-dark">Drop us a line</span>
</div>
<div class="footer-col" style="left:838px;width:200px">
  <h3>Contact</h3>
  <div class="contact-line"><svg width="10" height="14" viewBox="0 0 10 14"><path d="M5 0a5 5 0 0 1 5 5c0 4-5 9-5 9S0 9 0 5a5 5 0 0 1 5-5z" fill="#333"/><circle cx="5" cy="5" r="2" fill="#fff"/></svg><span>48 Harlow Parade,<br>Brookvale Heights, QLD 4230</span></div>
  <div class="contact-line"><svg width="12" height="12" viewBox="0 0 24 24"><path fill="#333" d="M6.6 10.8c1.4 2.8 3.8 5.1 6.6 6.6l2.2-2.2c.3-.3.7-.4 1-.2 1.1.4 2.3.6 3.6.6.6 0 1 .4 1 1V20c0 .6-.4 1-1 1C10.6 21 3 13.4 3 4c0-.6.4-1 1-1h3.5c.6 0 1 .4 1 1 0 1.3.2 2.5.6 3.6.1.3 0 .7-.2 1z"/></svg><span>1300 555 014</span></div>
  <div class="contact-line"><svg width="12" height="10" viewBox="0 0 12 10"><rect width="12" height="10" fill="#1f3b63"/><path d="M0 0l6 5 6-5" stroke="#fff" fill="none"/></svg><span>sales@velmoro.com.au</span></div>
  <div class="social"><span></span><span></span><span class="alt"></span></div>
</div>

<footer class="bottom-bar">Copyright © 2015 VELMORO.</footer>
<span class="to-top"><svg width="14" height="14" viewBox="0 0 14 14"><path d="M2 7l5-5 5 5M2 12l5-5 5 5" stroke="#fff" stroke-width="2" fill="none"/></svg></span>

</body>
</html>
```